Brenton Wealth Management Flow Charts

I need help creating three flow charts for my businesses website. We want them to be simple but look professional. This is for a Wealth Management firm. I will attach a word document that has all of the descriptions for everything so you know what icons to use. We just want the chart to have an icon, the names of each step and the corresponding numbers. I will also include some examples of charts we liked as well. Once the winner is selected, we will need help with additional graphic design elements for our website ASAP.
- Goudy Roman

```html
<!DOCTYPE html>
<html lang="en">
<head>
<meta charset="utf-8">
<title>The Retirement Planning Process</title>
<link href="https://fonts.googleapis.com/css2?family=Montserrat:wght@700&family=Oswald:wght@600;700&display=swap" rel="stylesheet">
<style>
  :root {
    --bg-a: #eef0f4;
    --bg-b: #f6f3f5;
    --bg-c: #d3dfe9;
    --title: #7a7a7a;
    --card: #ffffff;
    --teal: #30bfc8;   --teal-d: #24918d;
    --blue: #2f6d9c;   --blue-d: #244b68;
    --slate: #3c3b4d;  --slate-d: #121216;
    --plum: #8a3b5d;   --plum-d: #58223b;
    --red: #e9513c;    --red-d: #b2382a;
    --gold: #f8aa1c;   --gold-d: #d68c26;
  }
  * { margin: 0; padding: 0; box-sizing: border-box; }
  html, body { width: 1200px; height: 675px; overflow: hidden; }
  body {
    position: relative;
    background:
      radial-gradient(ellipse 700px 500px at 470px 320px, rgba(248,236,240,.7), transparent 70%),
      radial-gradient(ellipse 600px 420px at 1050px 120px, rgba(240,244,249,.9), transparent 70%),
      linear-gradient(160deg, var(--bg-a) 0%, var(--bg-b) 45%, var(--bg-c) 100%);
    font-family: "Oswald", "Arial Narrow", sans-serif;
  }
  .process-title {
    position: absolute;
    top: 182px; left: 0; width: 1200px;
    text-align: center;
    font-family: "Montserrat", Arial, sans-serif;
    font-weight: 700;
    font-size: 55px;
    letter-spacing: 0.5px;
    color: var(--title);
  }
  .steps { position: absolute; top: 324px; left: 60px; }
  .step {
    position: absolute; top: 0;
    width: 182px; height: 164px;
  }
  .step-shape {
    position: absolute; left: 0; top: 0;
    width: 182px; height: 164px;
    overflow: visible;
    filter: drop-shadow(0 5px 6px rgba(60,70,90,.28));
  }
  .card-body { fill: var(--card); }
  .tone-light { fill: var(--c); }
  .tone-dark { fill: var(--d); }
  .step-number {
    position: absolute; top: 7px; right: 31px;
    font-weight: 700; font-size: 23px; line-height: 1;
    color: var(--c);
  }
  .step-icon {
    position: absolute; left: 78px; top: 38px;
    width: 64px; height: 64px;
    fill: none; stroke: var(--c); stroke-width: 3.4;
    stroke-linecap: round; stroke-linejoin: round;
  }
  .step-label {
    position: absolute; right: 29px; bottom: 14px;
    font-weight: 700; font-size: 22px; line-height: 21px;
    text-align: right; text-transform: uppercase;
    letter-spacing: 0;
    color: var(--c);
    white-space: nowrap;
  }
  .step--discovery { left: 0;   --c: var(--teal);  --d: var(--teal-d); }
  .step--learning  { left: 180px; --c: var(--blue);  --d: var(--blue-d); }
  .step--planning  { left: 360px; --c: var(--slate); --d: var(--slate-d); }
  .step--execution { left: 541px; --c: var(--plum);  --d: var(--plum-d); }
  .step--alignment { left: 721px; --c: var(--red);   --d: var(--red-d); }
  .step--review    { left: 901px; --c: var(--gold);  --d: var(--gold-d); }
</style>
</head>
<body>
  <h1 class="process-title">THE RETIREMENT PLANNING PROCESS</h1>

  <svg width="0" height="0" style="position:absolute">
    <defs>
      <g id="step-frame">
        <path class="card-body" d="M12 0 H152 Q164 0 164 12 V151 Q164 163 152 163 H12 Q0 163 0 151 V128 L13 82 L0 36 V12 Q0 0 12 0 Z"/>
        <polygon class="tone-light" points="21,30 32,30 54,82 43,82"/>
        <polygon class="tone-dark" points="43,82 54,82 32,134 21,134"/>
        <polygon class="tone-light" points="164,62 180,82 164,82"/>
        <polygon class="tone-dark" points="164,82 180,82 164,102"/>
      </g>
    </defs>
  </svg>

  <div class="steps">
    <div class="step step--discovery">
      <svg class="step-shape" viewBox="0 0 182 164"><use href="#step-frame"/></svg>
      <span class="step-number">01</span>
      <svg class="step-icon" viewBox="0 0 64 64" aria-hidden="true">
        <path d="M12 30 C4 34 3 46 10 51 L8 58 L17 53 C24 56 32 54 35 49"/>
        <path d="M36 6 C50 6 58 15 58 26 C58 32 56 36 54 39 L57 48 L47 44 C44 45 40 46 36 46 C22 46 14 37 14 26 C14 15 22 6 36 6 Z"/>
        <line x1="26" y1="20" x2="46" y2="20"/>
        <line x1="26" y1="27" x2="46" y2="27"/>
        <line x1="26" y1="34" x2="38" y2="34"/>
      </svg>
      <span class="step-label">Discovery<br>Meeting</span>
    </div>

    <div class="step step--learning">
      <svg class="step-shape" viewBox="0 0 182 164"><use href="#step-frame"/></svg>
      <span class="step-number">02</span>
      <svg class="step-icon" viewBox="0 0 64 64" aria-hidden="true">
        <circle cx="32" cy="13" r="9"/>
        <path d="M16 36 C16 28 22 23 32 23 C42 23 48 28 48 36"/>
        <path d="M12 36 L32 42 L52 36 L52 56 L32 62 L12 56 Z"/>
        <line x1="32" y1="42" x2="32" y2="62"/>
        <path d="M12 42 H8 V50 H12 M52 42 H56 V50 H52"/>
      </svg>
      <span class="step-label">Learning</span>
    </div>

    <div class="step step--planning">
      <svg class="step-shape" viewBox="0 0 182 164"><use href="#step-frame"/></svg>
      <span class="step-number">03</span>
      <svg class="step-icon" viewBox="0 0 64 64" aria-hidden="true">
        <path d="M38 60 H14 Q10 60 10 56 V8 Q10 4 14 4 H48 Q52 4 52 8 V40"/>
        <path d="M6 14 H12 M6 26 H12 M6 38 H12 M6 50 H12"/>
        <path d="M18 14 L21 17 L26 11 M18 27 L21 30 L26 24 M18 40 L21 43 L26 37"/>
        <path d="M32 14 H44 M32 27 H44 M32 40 H38"/>
        <circle cx="50" cy="52" r="9"/>
        <path d="M50 47 V52 H54"/>
      </svg>
      <span class="step-label">Planning</span>
    </div>

    <div class="step step--execution">
      <svg class="step-shape" viewBox="0 0 182 164"><use href="#step-frame"/></svg>
      <span class="step-number">04</span>
      <svg class="step-icon" viewBox="0 0 64 64" aria-hidden="true">
        <path d="M28 4 H36 L37 11 L43 13 L48 8 L54 14 L50 20 L52 26 L60 27 V35 L52 36 L50 42 L54 48 L48 54 L43 50 L37 52 L36 60 H28 L27 52 L21 50 L16 54 L10 48 L14 42 L12 36 L4 35 V27 L12 26 L14 20 L10 14 L16 8 L21 13 L27 11 Z"/>
        <circle cx="32" cy="32" r="12"/>
        <path d="M26 32 L30 36 L38 28"/>
      </svg>
      <span class="step-label">Execution</span>
    </div>

    <div class="step step--alignment">
      <svg class="step-shape" viewBox="0 0 182 164"><use href="#step-frame"/></svg>
      <span class="step-number">05</span>
      <svg class="step-icon" viewBox="0 0 64 64" aria-hidden="true">
        <rect x="4" y="16" width="56" height="42" rx="3"/>
        <path d="M23 16 V10 Q23 7 26 7 H38 Q41 7 41 10 V16"/>
        <path d="M4 22 L26 38 M60 22 L38 38"/>
        <rect x="26" y="34" width="12" height="8" rx="1"/>
      </svg>
      <span class="step-label">Alignment</span>
    </div>

    <div class="step step--review">
      <svg class="step-shape" viewBox="0 0 182 164"><use href="#step-frame"/></svg>
      <span class="step-number">06</span>
      <svg class="step-icon" viewBox="0 0 64 64" aria-hidden="true">
        <circle cx="38" cy="24" r="18"/>
        <path d="M30 17 C32 13 36 12 40 12"/>
        <path d="M25 37 L8 54" stroke-width="7"/>
      </svg>
      <span class="step-label">Review</span>
    </div>
  </div>
</body>
</html>
```